HL - business card

Harbor Lane Brokers is an insurance brokerage firm, inovative, proactive, vigorous, which aims to become the leader of the insurance brokers in Anfrica. We should like to get some designs which should be avoided also in Gray / Metallic for the Administration and Orange / Blue for the Managers (ike in the picture sent). The Blue / Green logo is not the correct one, but the source of the file. Please adjust the color accordingly for the business cards. 1 / Orange / Blue 2 / Gray / Metallic We want something classic but which is transmitted strenght, inovation, modernity and most of all, rapidity. We want something start-up like, very punchy and catching eye remaining profesional at the same time. Name: Tobias Wendell Function: Managing Director Address: N ° 17/18 Rua Dovel - R / C 2B Direita - Bairro Sambelo - Luanda Tel: (+244) 947 385 610 Email: tobias.wendell@harbor-l.com Website: www.harbor-l. com We want classic in the front and creative, colorfull at the back. The cards will be printed in relief, with very high quality of paper.
Insurance Broker
Designer to choose colors to be used in the design.

```html
<!DOCTYPE html>
<html lang="en">
<head>
<meta charset="utf-8">
<title>Harbor Lane Brokers – Business Card</title>
<link href="https://fonts.googleapis.com/css2?family=Open+Sans:wght@400;700&display=swap" rel="stylesheet">
<style>
  :root {
    --backdrop: #3b3b3b;
    --card-black: #000000;
    --brand-grey: #6e6e6e;
    --name-grey: #8c8c8c;
    --ink: #1c1c1c;
    --icon-bg: #0a0a0a;
    --icon-fg: #ffffff;
  }
  html, body {
    margin: 0;
    padding: 0;
    width: 1200px;
    height: 1200px;
    overflow: hidden;
    background: var(--backdrop);
    font-family: "Open Sans", sans-serif;
  }
  .card {
    position: absolute;
    left: 252px;
    width: 724px;
    height: 416px;
    background: var(--card-black);
    overflow: hidden;
  }
  .card--front { top: 143px; }
  .card--back { top: 663px; }
  .card__waves {
    position: absolute;
    inset: 0;
    width: 724px;
    height: 416px;
  }
  .brand {
    position: absolute;
    display: flex;
    flex-direction: column;
    align-items: center;
    color: var(--brand-grey);
  }
  .brand__mark {
    border: 6px solid var(--brand-grey);
    border-radius: 50%;
    box-sizing: border-box;
  }
  .brand__name {
    font-weight: 700;
    white-space: nowrap;
    letter-spacing: 0.2px;
  }
  .card--front .brand { left: 0; right: 0; top: 58px; }
  .card--front .brand__mark { width: 116px; height: 116px; }
  .card--front .brand__name { font-size: 26px; margin-top: 14px; }
  .card--back .brand { left: 440px; width: 260px; top: 34px; }
  .card--back .brand__mark { width: 74px; height: 74px; border-width: 4px; }
  .card--back .brand__name { font-size: 17px; margin-top: 10px; }
  .holder {
    position: absolute;
    left: 45px;
    top: 64px;
  }
  .holder__name {
    margin: 0;
    font-weight: 400;
    font-size: 30px;
    line-height: 1;
    color: var(--name-grey);
  }
  .holder__rule {
    margin-top: 18px;
    margin-left: 21px;
    width: 169px;
    height: 3px;
    background: linear-gradient(90deg, #555 0 18px, #9a9a9a 18px 34px, #5a5a5a 34px);
  }
  .contact {
    position: absolute;
    display: flex;
    align-items: flex-start;
    gap: 12px;
    color: var(--ink);
    font-size: 16.5px;
    line-height: 21px;
  }
  .contact__icon {
    flex: none;
    width: 27px;
    height: 27px;
    border-radius: 50%;
    background: var(--icon-bg);
    display: flex;
    align-items: center;
    justify-content: center;
  }
  .contact__icon svg { width: 14px; height: 14px; fill: var(--icon-fg); }
  .contact--phone { left: 75px; top: 314px; }
  .contact--web { left: 75px; top: 360px; }
  .contact--email { left: 338px; top: 310px; }
  .contact--address { left: 338px; top: 352px; font-size: 14.5px; line-height: 21px; }
  .contact--phone .contact__text,
  .contact--web .contact__text { margin-top: 2px; }
</style>
</head>
<body>

<section class="card card--front">
  <svg class="card__waves" viewBox="0 0 724 416" aria-hidden="true">
    <defs>
      <linearGradient id="base-front" x1="0" x2="1" y1="0" y2="0">
        <stop offset="0" stop-color="#0a0a0a"/>
        <stop offset="0.45" stop-color="#777"/>
        <stop offset="1" stop-color="#d2d2d2"/>
      </linearGradient>
      <linearGradient id="veil-front" x1="0" x2="1" y1="0" y2="0">
        <stop offset="0" stop-color="#fff" stop-opacity="0.05"/>
        <stop offset="1" stop-color="#fff" stop-opacity="0.45"/>
      </linearGradient>
    </defs>
    <path d="M0 270 C120 250 220 300 330 290 C460 278 520 235 724 258 L724 416 L0 416 Z" fill="url(#veil-front)" opacity="0.5"/>
    <path d="M0 300 C140 260 260 330 400 300 C520 275 600 265 724 290 L724 416 L0 416 Z" fill="url(#veil-front)" opacity="0.6"/>
    <path d="M0 320 C110 300 230 280 360 305 C480 330 600 300 724 280 L724 416 L0 416 Z" fill="url(#veil-front)" opacity="0.5"/>
    <path d="M0 335 C150 330 300 345 460 330 C580 320 650 310 724 312 L724 416 L0 416 Z" fill="url(#base-front)"/>
  </svg>
  <div class="brand">
    <div class="brand__mark"></div>
    <div class="brand__name">HARBOR LANE BROKERS</div>
  </div>
</section>

<section class="card card--back">
  <svg class="card__waves" viewBox="0 0 724 416" aria-hidden="true">
    <defs>
      <linearGradient id="base-back" x1="0" x2="1" y1="0" y2="0">
        <stop offset="0" stop-color="#0a0a0a"/>
        <stop offset="0.45" stop-color="#8a8a8a"/>
        <stop offset="1" stop-color="#d2d2d2"/>
      </linearGradient>
      <linearGradient id="veil-back" x1="0" x2="1" y1="0" y2="0">
        <stop offset="0" stop-color="#fff" stop-opacity="0.05"/>
        <stop offset="1" stop-color="#fff" stop-opacity="0.45"/>
      </linearGradient>
    </defs>
    <path d="M0 218 C120 200 220 250 330 240 C460 228 520 188 724 206 L724 416 L0 416 Z" fill="url(#veil-back)" opacity="0.5"/>
    <path d="M0 250 C140 210 260 280 400 250 C520 225 600 215 724 240 L724 416 L0 416 Z" fill="url(#veil-back)" opacity="0.6"/>
    <path d="M0 268 C110 248 230 228 360 253 C480 278 600 248 724 228 L724 416 L0 416 Z" fill="url(#veil-back)" opacity="0.5"/>
    <path d="M0 290 C150 284 300 296 460 282 C580 272 650 264 724 266 L724 416 L0 416 Z" fill="url(#base-back)"/>
  </svg>

  <div class="holder">
    <h1 class="holder__name">Tobias Wendell</h1>
    <div class="holder__rule"></div>
  </div>

  <div class="brand">
    <div class="brand__mark"></div>
    <div class="brand__name">HARBOR LANE BROKERS</div>
  </div>

  <div class="contact contact--phone">
    <span class="contact__icon"><svg viewBox="0 0 24 24"><path d="M6.6 10.8a15 15 0 0 0 6.6 6.6l2.2-2.2c.3-.3.7-.4 1-.2 1.1.4 2.3.6 3.6.6.6 0 1 .4 1 1V20c0 .6-.4 1-1 1A17 17 0 0 1 3 4c0-.6.4-1 1-1h3.5c.6 0 1 .4 1 1 0 1.3.2 2.5.6 3.6.1.3 0 .7-.2 1z"/></svg></span>
    <span class="contact__text">(+244) 947 385 610</span>
  </div>
  <div class="contact contact--web">
    <span class="contact__icon"><svg viewBox="0 0 24 24"><path d="M5 2l14 10-6 1.2 3.5 7-2.6 1.3-3.5-7L5 19z"/></svg></span>
    <span class="contact__text">www.harbor-l. com</span>
  </div>
  <div class="contact contact--email">
    <span class="contact__icon"><svg viewBox="0 0 24 24"><path d="M3 5h18v14H3z M4.5 6.5l7.5 6 7.5-6" fill="none" stroke="#fff" stroke-width="0"/><path d="M3 5h18v2l-9 6-9-6z M3 9l9 6 9-6v10H3z"/></svg></span>
    <span class="contact__text">tobias.wendell@harbor-l.com</span>
  </div>
  <div class="contact contact--address">
    <span class="contact__icon"><svg viewBox="0 0 24 24"><path d="M12 2a7 7 0 0 0-7 7c0 5.3 7 13 7 13s7-7.7 7-13a7 7 0 0 0-7-7zm0 9.5A2.5 2.5 0 1 1 12 6.5a2.5 2.5 0 0 1 0 5z"/></svg></span>
    <span class="contact__text">N ° 17/18 Rua Dovel - R / C 2B Direita<br>Bairro Sambelo - Luanda</span>
  </div>
</section>

</body>
</html>
```